Law Firm Website

We are a small California based law firm specializing in business, corporate and litigation matters. We need to have our website redesigned. We are looking for a new and fresh look for our site, keeping in mind that we are a law firm.
What we don't want:
**the traditional "gavel" and "scales of justice" look
**anything too crazy
What we do want:
**sophisticated yet modern and fresh corporate look and feel
**samples of websites we really like:
http://www.tkrmllp.example
http://www.hollowaybrant.example/
we also like:
http://www.fentonardis.example/
http://www.qx.example/
http://www.moberly.example/
http://www.pvtr.example
http://www.npdlaw.example/
The content will be whatever is currently on our website (www.colterlawgroup.example). We will be selecting the winner based on originality and keeping the above requirements in mind. Please note that the photos that you use will be the ones that we will be using, so choose wisely because the photos will make a difference.
Target Market(s)
Corporate clients
Industry/Entity Type
Law Firm
Look and feel

```html
<!DOCTYPE html>
<html lang="en">
<head>
<meta charset="utf-8">
<title>Colter Law Group, LLP</title>
<link href="https://fonts.googleapis.com/css2?family=Montserrat:wght@400&family=Noto+Serif:wght@400&family=Open+Sans:wght@400;700&family=Roboto+Slab:wght@300;400&display=swap" rel="stylesheet">
<style>
  :root {
    --blue: #1676c2;
    --link: #0d6fb8;
    --text: #6b6b6b;
    --dark: #3a3a3a;
    --nav: #555a60;
    --header-bg: #f7f8f9;
    --footer-bg: #f1f2f3;
    --panel-bg: #f6f7f7;
    --frame: #e4e4e4;
    --rule: #e6e8ea;
  }
  * { box-sizing: border-box; margin: 0; padding: 0; }
  html, body { width: 1200px; height: 949px; overflow: hidden; background: #fff; }
  body { position: relative; font-family: "Open Sans", sans-serif; color: var(--text); }

  .site-header { position: absolute; left: 0; top: 0; width: 1200px; height: 124px; background: var(--header-bg); border-bottom: 1px solid var(--rule); }
  .brand { position: absolute; left: 140px; top: 24px; display: flex; align-items: center; gap: 10px; }
  .brand-mark { width: 83px; height: 83px; background: var(--blue); }
  .brand-name { font-family: "Noto Serif", serif; font-size: 17px; line-height: 21px; color: var(--blue); font-weight: 400; }
  .main-nav { position: absolute; right: 141px; top: 57px; display: flex; gap: 41px; }
  .main-nav a { font-family: "Montserrat", sans-serif; font-size: 12.5px; color: var(--nav); text-decoration: none; letter-spacing: .2px; }
  .main-nav a.active { color: var(--blue); }

  .hero { position: absolute; left: 140px; top: 154px; width: 919px; height: 375px; overflow: hidden; }
  .hero-photo { position: absolute; inset: 0; background: linear-gradient(90deg, #6f7785 0%, #8a93a0 28%, #5d6576 52%, #4a5063 70%, #484d62 100%); }
  .hero-copy { position: absolute; left: 520px; top: 34px; width: 360px; color: #fff; }
  .hero-title { font-family: "Roboto Slab", serif; font-weight: 300; font-size: 44px; line-height: 51px; width: 330px; }
  .hero-rule { width: 309px; height: 1px; background: rgba(255,255,255,.6); margin: 7px 0 0 8px; }
  .hero-text { font-family: "Montserrat", sans-serif; font-size: 12.5px; line-height: 21px; margin: 24px 0 0 8px; width: 352px; }
  .slider-arrow { position: absolute; top: 176px; width: 41px; height: 41px; background: rgba(255,255,255,.92); display: flex; align-items: center; justify-content: center; }
  .slider-arrow.prev { left: 0; }
  .slider-arrow.next { right: 0; }

  .column { position: absolute; top: 562px; width: 282px; }
  .column h2 { font-size: 15px; font-weight: 700; color: var(--blue); text-transform: uppercase; line-height: 20px; margin-bottom: 16px; }
  .thumb { width: 281px; height: 129px; background: var(--frame); padding: 5px; }
  .thumb div { width: 100%; height: 100%; }
  .column p { font-size: 13px; line-height: 21px; margin-top: 14px; }
  .read-more { display: inline-block; margin-top: 5px; font-size: 13px; color: var(--link); text-decoration: none; }

  .news { position: absolute; left: 777px; top: 598px; width: 282px; height: 247px; background: var(--panel-bg); padding: 16px 19px 0 19px; }
  .news-item { border-bottom: 1px dotted #cfd3d6; padding-bottom: 19px; margin-bottom: 15px; }
  .news-item:last-child { border-bottom: none; }
  .news-date { font-size: 12.5px; color: #7c7c7c; line-height: 18px; }
  .news-text { font-size: 13.5px; line-height: 21px; color: var(--text); margin-top: 6px; }
  .news-more { display: block; text-align: right; font-size: 13px; color: var(--link); margin-top: 2px; }

  .site-footer { position: absolute; left: 0; top: 894px; width: 1200px; height: 55px; background: var(--footer-bg); }
  .footer-nav { position: absolute; left: 140px; top: 19px; display: flex; gap: 37px; }
  .footer-nav a { font-size: 13px; color: var(--dark); text-decoration: none; }
  .copyright { position: absolute; right: 141px; top: 17px; font-size: 13px; color: #7a7a7a; }
</style>
</head>
<body>
  <header class="site-header">
    <div class="brand">
      <div class="brand-mark"></div>
      <div class="brand-name">Colter Law Group, LLP<br>Attorneys at Law</div>
    </div>
    <nav class="main-nav">
      <a class="active" href="#">HOME</a>
      <a href="#">ABOUT CLG</a>
      <a href="#">PRACTICE AREAS</a>
      <a href="#">LINKS</a>
      <a href="#">CONTACT</a>
    </nav>
  </header>

  <section class="hero">
    <div class="hero-photo" role="img" aria-label="Businessman in a grey suit and striped tie with arms crossed"></div>
    <div class="hero-copy">
      <h1 class="hero-title">Lorem Ipsum is Simple Dummy Text</h1>
      <div class="hero-rule"></div>
      <p class="hero-text">Colter Law Group, LLP provides quality legal representation to corporate as well as individual clients in the areas of business, corporate, securities . . . .</p>
    </div>
    <a class="slider-arrow prev" href="#" aria-label="Previous slide">
      <svg width="16" height="26" viewBox="0 0 16 26"><path d="M13 2 L3 13 L13 24" fill="none" stroke="#4a4f5c" stroke-width="2.5"/></svg>
    </a>
    <a class="slider-arrow next" href="#" aria-label="Next slide">
      <svg width="16" height="26" viewBox="0 0 16 26"><path d="M3 2 L13 13 L3 24" fill="none" stroke="#4a4f5c" stroke-width="2.5"/></svg>
    </a>
  </section>

  <section class="column" style="left:140px">
    <h2>Welcome to CLG</h2>
    <div class="thumb"><div role="img" aria-label="Bright law office reception with chairs and desks" style="background:linear-gradient(180deg,#e9e6df 0%,#d8d2c6 55%,#8a5a3c 100%)"></div></div>
    <p>Colter Law Group, LLP takes pride in providing quality legal representation to its clients, whether they are large corporations, partnerships, or individuals.</p>
    <a class="read-more" href="#">[ Read More ]</a>
  </section>

  <section class="column" style="left:459px">
    <h2>Practice Area</h2>
    <div class="thumb"><div role="img" aria-label="Row of old leather-bound law books" style="background:linear-gradient(90deg,#5a2e17 0%,#b07a2e 35%,#7a3a1f 60%,#c89a4a 85%,#6b3a1e 100%)"></div></div>
    <p>The key to your success is having the right team supporting you.&nbsp; Our attorneys can provide a key component: aggressive legal representation.&nbsp; We represent clients in a . . .</p>
    <a class="read-more" href="#">[ Read More ]</a>
  </section>

  <section class="column" style="left:779px">
    <h2>Latest News</h2>
  </section>
  <div class="news">
    <div class="news-item">
      <div class="news-date">20,september, 2012</div>
      <div class="news-text">Lorem Ipsum is simply dummy text of the printing and typesetting</div>
      <a class="news-more" href="#">Read More</a>
    </div>
    <div class="news-item">
      <div class="news-date">20,september, 2012</div>
      <div class="news-text">Lorem Ipsum is simply dummy text of the printing and typesetting</div>
      <a class="news-more" href="#">Read More</a>
    </div>
  </div>

  <footer class="site-footer">
    <nav class="footer-nav">
      <a href="#">Home</a>
      <a href="#">About CLG</a>
      <a href="#">Practice Areas</a>
      <a href="#">Links</a>
      <a href="#">Contact</a>
    </nav>
    <div class="copyright">© 2014 Colter Law Group. All Right Reserved</div>
  </footer>
</body>
</html>
```